Insurance company needs a business card design

We need a business card design for a Massachusetts-based insurance company Veloria Insurance, LLC. We provide auto insurance to Hispanic (Spanish- or Portuguese-speaking) immigrants in the United States. We will give these business cards to auto dealers where such customers typically go to purchase vehicles. We will provide a solution to the dealers to provide easy insurance to the customers buying cars at their dealerships. Veloria is the Spanish word for protection.
Contact Information for Business Card
Name, Designation, Company Name, Address, Phone Number, Email, Website
Look and feel
Each slider illustrates characteristics of the customer's brand and the style your logo design should communicate.

```html
<!DOCTYPE html>
<html lang="en">
<head>
<meta charset="utf-8">
<title>Veloria Insurance – Business Card</title>
<link href="https://fonts.googleapis.com/css2?family=Montserrat:ital,wght@0,400;0,600;0,800;1,400;1,800&display=swap" rel="stylesheet">
<style>
  :root{
    --bg:#ececec;
    --navy:#004f80;
    --navy-deep:#00456f;
    --orange:#ef7d00;
    --text:#4a4f55;
    --white:#ffffff;
  }
  *{box-sizing:border-box;margin:0;padding:0}
  html,body{width:1200px;height:790px;overflow:hidden;background:var(--bg);font-family:"Montserrat",sans-serif}
  .canvas{position:relative;width:1200px;height:790px}

  .card{position:absolute;top:232px;width:480px;height:274px;overflow:hidden}
  .card-front{left:103px;background:linear-gradient(180deg,#00679a 0%,var(--navy) 100%)}
  .card-back{left:611px;background:var(--white)}

  .brand{position:absolute;display:flex;align-items:center;gap:8px;font-weight:800;letter-spacing:.02em;white-space:nowrap}
  .brand-mark{display:inline-block;background:var(--orange)}
  .front-brand{left:42px;top:118px;font-size:30px;color:var(--white)}
  .front-brand .brand-mark{width:22px;height:22px}

  .holder-name{position:absolute;left:48px;top:42px;font-size:19px;font-weight:800;color:var(--navy);letter-spacing:.02em}
  .holder-role{position:absolute;left:48px;top:64px;font-size:11.5px;font-weight:400;color:var(--orange);letter-spacing:.03em}

  .contact{position:absolute;left:49px;top:130px;list-style:none;font-size:11.5px;color:var(--text);letter-spacing:.03em;line-height:14px}
  .contact li{display:flex;align-items:flex-start;gap:5px}
  .contact .addr{margin-bottom:3px}
  .contact svg{width:9px;height:11px;flex:none;margin-top:2px;fill:var(--navy)}

  .accent-bar{position:absolute;left:49px;top:207px;width:272px;height:9px;background:var(--orange)}
  .website{position:absolute;left:48px;top:220px;font-size:11px;font-style:italic;color:var(--navy);letter-spacing:.02em}
  .website strong{font-weight:800}

  .back-brand{right:46px;top:110px;width:160px;font-size:14px;color:var(--navy);flex-direction:column;align-items:center;gap:40px;letter-spacing:.01em}
  .back-brand .brand-mark{width:30px;height:30px}
</style>
</head>
<body>
<main class="canvas">

  <section class="card card-front" aria-label="Card front">
    <div class="brand front-brand"><span class="brand-mark"></span>Veloria Insurance</div>
  </section>

  <section class="card card-back" aria-label="Card back">
    <h1 class="holder-name">DANIEL REYES</h1>
    <p class="holder-role">President</p>

    <ul class="contact">
      <li class="addr">
        <svg viewBox="0 0 10 13"><path d="M5 0a4.5 4.5 0 0 0-4.5 4.5C.5 8 5 13 5 13s4.5-5 4.5-8.5A4.5 4.5 0 0 0 5 0zm0 6.3a1.8 1.8 0 1 1 0-3.6 1.8 1.8 0 0 1 0 3.6z"/></svg>
        <span>2140 Harbor View Road<br>Springfield, Mass. 01103</span>
      </li>
      <li>
        <svg viewBox="0 0 12 12"><path d="M2.4 0 4.3 2.4 3.2 4a7 7 0 0 0 4.8 4.8l1.6-1.1L12 9.6 10.6 12C5 12 0 7 0 1.4z"/></svg>
        <span>555-214-7730</span>
      </li>
      <li>
        <svg viewBox="0 0 8 12"><path d="M1 0h6a1 1 0 0 1 1 1v10a1 1 0 0 1-1 1H1a1 1 0 0 1-1-1V1a1 1 0 0 1 1-1zm.4 1.4v8h5.2v-8zM4 10a.6.6 0 1 0 0 1.2A.6.6 0 0 0 4 10z"/></svg>
        <span>555-389-1642</span>
      </li>
      <li>
        <svg viewBox="0 0 12 9" style="margin-top:3px"><path d="M0 0h12v9H0zm1.2 1.2v.3L6 5l4.8-3.5v-.3zm0 1.8v4.8h9.6V3L6 6.5z"/></svg>
        <span>info@veloriainsurance.com</span>
      </li>
    </ul>

    <div class="accent-bar"></div>
    <p class="website">www.<strong>VeloriaInsurance</strong>.com</p>

    <div class="brand back-brand"><span class="brand-mark"></span>Veloria Insurance</div>
  </section>

</main>
</body>
</html>
```